Website design using a wordpress template I purchased

I have purchased a wordpress template called "Vantrel" from Plumora and would like to design a website using it for a financial services company. The site simply needs to be informational about the company and a blog. Nothing too involved. The company provides paymaster / escrow services for commodity transactions. I am working on the logo currently and will have it ready to provide shortly. I can provide the content for the informational portion of the site as well. I would like some quick tutoring regarding how to administer the blog portion of the site once built.

```html
<!DOCTYPE html>
<html lang="en">
<head>
<meta charset="utf-8">
<title>Ledgerbay Finance</title>
<link rel="stylesheet" href="https://fonts.googleapis.com/css2?family=DM+Serif+Display&family=Mulish:wght@400;600;700;800&display=swap">
<style>
:root{
  --blue:#0096d6;
  --ink:#2b2b2b;
  --muted:#444;
  --panel:#f5f4f4;
  --footer:#2f2f2f;
  --white:#fff;
  --serif:"DM Serif Display",Georgia,serif;
  --sans:"Mulish",Arial,sans-serif;
}
*{box-sizing:border-box;margin:0;padding:0}
html,body{width:1200px;height:3093px;overflow:hidden}
body{position:relative;font-family:var(--sans);color:var(--ink);background:var(--white)}
.abs{position:absolute}
.serif{font-family:var(--serif);font-weight:400}
.center{text-align:center}
.btn{position:absolute;display:flex;align-items:center;justify-content:center;font-family:var(--sans);font-weight:800;text-transform:uppercase;background:var(--blue);color:var(--white)}
.btn.light{background:var(--white);color:var(--blue)}

/* hero */
.hero{left:0;top:0;width:1200px;height:658px;background:linear-gradient(135deg,#5a4130 0%,#7a5a40 35%,#4e3a2c 65%,#2c2520 100%)}
.hero::after{content:"";position:absolute;inset:0;background:rgba(0,0,0,.25)}
.hero-photo{position:absolute;inset:0}
.brand{left:134px;top:27px;font-family:var(--sans);font-weight:700;font-size:22px;color:var(--white);z-index:2}
.nav{left:652px;top:23px;display:flex;z-index:2}
.nav a{font-size:16px;color:var(--white);text-decoration:none;height:25px;line-height:25px;padding:0 8px;margin-right:20px}
.nav a.active{background:var(--blue)}
.hero-title{left:0;width:1200px;top:218px;font-size:53px;line-height:60px;color:var(--white);z-index:2}
.hero .btn{left:532px;top:364px;width:137px;height:46px;font-size:16px;z-index:2}
.dots{left:568px;top:547px;display:flex;gap:6px;z-index:2}
.dots span{width:12px;height:12px;border:1.5px solid var(--white);border-radius:50%}
.dots span.on{background:var(--blue)}

/* service cards */
.svc{top:605px;width:299px;height:316px;background:var(--blue);color:var(--white);text-align:center;padding-top:24px}
.svc .icon{height:66px;display:flex;align-items:center;justify-content:center}
.svc h3{font-family:var(--serif);font-weight:400;font-size:19px;line-height:24px;margin-top:20px}
.svc p{font-size:12.5px;line-height:17px;width:222px;margin:20px auto 0}
.svc .btn{left:106px;bottom:35px;width:86px;height:28px;font-size:10px}

/* why */
.why-h{left:0;width:1200px;top:980px;font-size:22px}
.why-p{left:0;width:1200px;top:1040px;font-size:15px;line-height:24px;color:var(--muted)}
.feat{top:1135px;width:260px;text-align:center}
.feat .icon{height:56px;display:flex;align-items:center;justify-content:center}
.feat h4{font-family:var(--serif);font-weight:400;font-size:18px;line-height:24px;margin-top:20px}
.feat p{font-size:12.5px;line-height:17px;margin-top:14px;color:var(--ink)}

/* about */
.about-img{left:0;top:1370px;width:561px;height:447px;background:linear-gradient(160deg,#8aa6c6 0%,#5e7898 45%,#3a4a60 75%,#a08468 100%)}
.about-panel{left:561px;top:1370px;width:639px;height:447px;background:var(--panel)}
.about-h{left:628px;top:1412px;font-size:22px}
.rule{height:2px;background:var(--ink)}
.about-p{left:628px;top:1480px;width:432px;font-size:14px;line-height:21.6px;color:var(--muted)}
.about-btn{left:631px;top:1722px;width:110px;height:36px;font-size:13px}

/* blog */
.blog{left:0;top:1817px;width:1200px;height:643px;background:linear-gradient(180deg,#eef1f4 0%,#f3f5f7 60%,#eef0f3 100%)}
.blog-h{left:0;width:1222px;top:1870px;font-size:22px}
.post{top:1965px;width:304px;height:431px;background:var(--white);box-shadow:0 2px 8px rgba(0,0,0,.06)}
.post .ph{height:183px}
.post h5{font-family:var(--serif);font-weight:400;font-size:14.5px;line-height:17px;margin:30px 28px 0;width:220px}
.post p{font-size:11px;line-height:16px;margin:20px 28px 0;color:var(--muted)}
.post .btn{left:31px;top:365px;width:92px;height:29px;font-size:10.5px}

/* cta */
.cta{left:0;top:2460px;width:1200px;height:297px;background:var(--blue);color:var(--white)}
.cta-h{left:0;width:1200px;top:48px;font-size:25px;line-height:33px}
.cta-p{left:0;width:1200px;top:132px;font-size:17px;line-height:22px}
.cta .btn{left:539px;top:207px;width:122px;height:41px;font-size:13px}

/* footer */
.foot{left:0;top:2757px;width:1200px;height:336px;background:var(--footer);color:var(--white)}
.foot-brand{left:132px;top:106px;font-family:var(--sans);font-weight:700;font-size:27px}
.foot h6{position:absolute;font-size:13px;font-weight:800;letter-spacing:.3px}
.contact-row{position:absolute;left:426px;display:flex;gap:10px;align-items:center;font-size:12px;line-height:15px}
.ico{width:24px;height:24px;border-radius:50%;background:#e9e9e9;display:flex;align-items:center;justify-content:center;flex:none}
.menu{position:absolute;left:782px;top:70px;list-style:none;font-size:12px;line-height:24px;text-transform:uppercase}
.social{position:absolute;left:957px;display:flex;gap:10px;align-items:center;font-size:12px;line-height:15px}
.divider{left:120px;top:258px;width:937px;height:1px;background:#4a4a4a}
.copy{left:0;width:1200px;top:296px;font-size:11px}
</style>
</head>
<body>

<!-- hero -->
<section class="abs hero">
  <div class="hero-photo" role="img" aria-label="Overhead photo of a desk with financial charts, notes, a laptop and a calculator"></div>
  <div class="abs brand">Ledgerbay Finance</div>
  <nav class="abs nav">
    <a class="active">Home</a><a>About Us</a><a>Services</a><a>Blog</a><a>Contact us</a>
  </nav>
  <h1 class="abs hero-title serif center">Welcome to<br>Financial Services</h1>
  <a class="btn">Read More</a>
  <div class="abs dots"><span></span><span class="on"></span><span></span><span></span></div>
</section>

<!-- service cards -->
<div class="abs svc" style="left:132px">
  <div class="icon">
  <svg width="58" height="66" viewBox="0 0 58 66" fill="none" stroke="#fff" stroke-width="3">
    <path d="M9 44a24 24 0 0 1 26-36"/><path d="M49 22a24 24 0 0 1-26 36"/>
    <path d="M30 3l6 5-6 5M28 63l-6-5 6-5"/>
    <circle cx="29" cy="33" r="13" fill="#fff" stroke="none"/>
    <text x="29" y="40" text-anchor="middle" font-family="Arial" font-weight="700" font-size="19" fill="#0096d6" stroke="none">$</text>
  </svg>
  </div>
  <h3>Cashback Checking</h3>
  <p>There are many variations of passages of Lorem Ipsum available, but the majority have suffered alteration in some form by injected humour, or randomised.</p>
  <a class="btn light">Read More</a>
</div>
<div class="abs svc" style="left:453px">
  <div class="icon">
  <svg width="62" height="66" viewBox="0 0 62 66">
    <ellipse cx="30" cy="46" rx="25" ry="17" fill="#fff"/>
    <rect x="14" y="56" width="7" height="9" fill="#fff"/><rect x="38" y="56" width="7" height="9" fill="#fff"/>
    <circle cx="31" cy="16" r="11" fill="none" stroke="#fff" stroke-width="3"/>
    <text x="31" y="22" text-anchor="middle" font-family="Arial" font-weight="700" font-size="16" fill="#fff">$</text>
    <circle cx="18" cy="42" r="2" fill="#0096d6"/>
  </svg>
  </div>
  <h3>Savings</h3>
  <p>There are many variations of passages of Lorem Ipsum available, but the majority have suffered alteration in some form by injected humour, or randomised.</p>
  <a class="btn light">Read More</a>
</div>
<div class="abs svc" style="left:769px">
  <div class="icon">
  <svg width="56" height="60" viewBox="0 0 56 60">
    <rect x="2" y="4" width="52" height="40" rx="5" fill="#fff"/>
    <path d="M10 34l12-12 8 8 16-16" fill="none" stroke="#0096d6" stroke-width="4"/>
    <rect x="26" y="44" width="4" height="10" fill="#fff"/><rect x="12" y="54" width="32" height="3" fill="#fff"/>
  </svg>
  </div>
  <h3>Financial Services</h3>
  <p>There are many variations of passages of Lorem Ipsum available, but the majority have suffered alteration in some form by injected humour, or randomised.</p>
  <a class="btn light">Read More</a>
</div>

<!-- why choose us -->
<h2 class="abs why-h serif center">Why Choose Us?</h2>
<p class="abs why-p center">It is a long established fact that a reader will be distracted by the readable content of a page when<br>Many desktop publishing packages and web page editors now use Lorem Ipsum</p>

<div class="abs feat" style="left:137px">
  <div class="icon">
  <svg width="54" height="56" viewBox="0 0 54 56" fill="none" stroke="#0096d6" stroke-width="4">
    <path d="M8 30V24a19 19 0 0 1 38 0v6"/>
    <rect x="4" y="28" width="10" height="18" rx="4" fill="#0096d6"/><rect x="40" y="28" width="10" height="18" rx="4" fill="#0096d6"/>
    <path d="M45 46q0 8-14 8"/>
  </svg>
  </div>
  <h4>Support</h4>
  <p>There are many variations of passages of Lorem Ipsum available, but the majority have suffered alteration in some form.</p>
</div>
<div class="abs feat" style="left:469px">
  <div class="icon">
  <svg width="58" height="54" viewBox="0 0 58 54" fill="none" stroke="#0096d6" stroke-width="4">
    <rect x="3" y="14" width="52" height="36" rx="5"/><path d="M20 14V6h18v8M3 28h52"/><rect x="25" y="24" width="8" height="8" fill="#0096d6"/>
  </svg>
  </div>
  <h4>Experience</h4>
  <p>There are many variations of passages of Lorem Ipsum available, but the majority have suffered alteration in some form.</p>
</div>
<div class="abs feat" style="left:809px">
  <div class="icon">
  <svg width="58" height="56" viewBox="0 0 58 56">
    <rect x="6" y="24" width="12" height="28" rx="2" fill="#0096d6"/>
    <path d="M22 26l10-18q6 0 5 8l-2 8h14q6 0 5 6l-4 18q-1 4-6 4H22z" fill="none" stroke="#0096d6" stroke-width="3.5"/>
    <path d="M10 2l2 5 5 0-4 3 2 5-5-3-5 3 2-5-4-3 5 0z" fill="#0096d6"/>
  </svg>
  </div>
  <h4>Excellence</h4>
  <p>There are many variations of passages of Lorem Ipsum available, but the majority have suffered alteration in some form.</p>
</div>

<!-- about -->
<div class="abs about-img" role="img" aria-label="Photo of a business team meeting around a table in a glass office"></div>
<div class="abs about-panel"></div>
<h2 class="abs about-h serif">About Us</h2>
<div class="abs rule" style="left:628px;top:1454px;width:154px"></div>
<p class="abs about-p">There are many variations of passages of Lorem Ipsum available, but the majority have suffered alteration in some form, by injected humour, or randomised words which don't look even slightly believable. If you are going to use a passage of Lorem Ipsum, you need to be sure there isn't anything embarrassing hidden in the middle of text. All the Lorem Ipsum generators on the Internet tend to repeat predefined chunks as necessary, making this the first true generator on the Internet. It uses a dictionary of over 200 Latin words, combined with a handful of model sentence structures, to generate Lorem Ipsum which looks reasonable.</p>
<a class="btn about-btn">Read More</a>

<!-- blog -->
<section class="abs blog" role="img" aria-label="Faint photo of an office interior behind the blog section"></section>
<h2 class="abs blog-h serif center">Latest Blog</h2>
<div class="abs rule" style="left:560px;top:1918px;width:102px"></div>

<article class="abs post" style="left:132px">
  <div class="ph" role="img" aria-label="Photo of two people shaking hands over a desk with a gavel" style="background:linear-gradient(120deg,#2a2d33 0%,#6b6c70 45%,#d8d6d2 70%,#3a3c42 100%)"></div>
  <h5>Lorem Ipsum is simply dummy text of the printing</h5>
  <p>There are many variations of passages of Lorem Ipsum available, but the majority have suffered alteration in some form, by injected humour, or randomised words which don't look even slightly believable.</p>
  <a class="btn">Read More</a>
</article>
<article class="abs post" style="left:448px">
  <div class="ph" role="img" aria-label="Photo collage of financial charts and a city skyline" style="background:linear-gradient(120deg,#8a6a52 0%,#5e6a76 40%,#3c4652 70%,#7d8690 100%)"></div>
  <h5>Lorem Ipsum is simply dummy text of the printing</h5>
  <p>There are many variations of passages of Lorem Ipsum available, but the majority have suffered alteration in some form, by injected humour, or randomised words which don't look even slightly believable.</p>
  <a class="btn">Read More</a>
</article>
<article class="abs post" style="left:765px">
  <div class="ph" role="img" aria-label="Overhead photo of a desk with charts, notes and a laptop" style="background:linear-gradient(120deg,#6d4c36 0%,#9c7a5e 40%,#c8bfb3 60%,#5a4232 100%)"></div>
  <h5>Lorem Ipsum is simply dummy text of the printing</h5>
  <p>There are many variations of passages of Lorem Ipsum available, but the majority have suffered alteration in some form, by injected humour, or randomised words which don't look even slightly believable.</p>
  <a class="btn">Read More</a>
</article>

<!-- call to action -->
<section class="abs cta">
  <h2 class="abs cta-h serif center">There are many variations of passages of Lorem Ipsum available<br>but the majority have suffered alteration</h2>
  <p class="abs cta-p center">There are many variations of passages of Lorem Ipsum available but the majority have<br>suffered alteration in some form, by injected humour, or randomised.</p>
  <a class="btn light">Contact Us</a>
</section>

<!-- footer -->
<footer class="abs foot">
  <div class="abs foot-brand">Ledgerbay Finance</div>

  <h6 style="left:426px;top:40px">CONTACT US</h6>
  <div class="contact-row" style="top:80px">
    <span class="ico"><svg width="12" height="14" viewBox="0 0 12 14"><path d="M6 0a5 5 0 0 1 5 5c0 4-5 9-5 9S1 9 1 5a5 5 0 0 1 5-5z" fill="#2f2f2f"/><circle cx="6" cy="5" r="2" fill="#e9e9e9"/></svg></span>
    <span>Suite 204, Level 2 West,<br>415-429 Harlow Street, Brenton VIC 3190.</span>
  </div>
  <div class="contact-row" style="top:131px">
    <span class="ico"><svg width="12" height="12" viewBox="0 0 12 12"><path d="M2 0l3 3-1.5 2a7 7 0 0 0 3.5 3.5L9 7l3 3-2 2C5 12 0 7 0 2z" fill="#2f2f2f"/></svg></span>
    <span>Call Us<br>+1 555 014 2290</span>
  </div>
  <div class="contact-row" style="top:182px">
    <span class="ico"><svg width="12" height="10" viewBox="0 0 12 10"><rect width="12" height="9" rx="1" fill="#2f2f2f"/><path d="M0 1l6 4 6-4" fill="none" stroke="#e9e9e9" stroke-width="1.2"/></svg></span>
    <span>E mail Us<br>info@ledgerbayfinance.com</span>
  </div>

  <h6 style="left:782px;top:40px">MENU</h6>
  <ul class="menu"><li>Home</li><li>About Us</li><li>Services</li><li>Blog</li><li>Contact Us</li></ul>

  <h6 style="left:959px;top:40px">FOLLOW US</h6>
  <div class="social" style="top:92px"><span class="ico"></span><span>Like us on<br>KINDRED</span></div>
  <div class="social" style="top:142px"><span class="ico"></span><span>Follow us on<br>CHIRPER</span></div>
  <div class="social" style="top:193px"><span class="ico"></span><span>Follow us on<br>WORKLINK</span></div>

  <div class="abs divider"></div>
  <div class="abs copy center">Copyright © 2022 All Rights Reserved</div>
</footer>

</body>
</html>
```